Web form face-lift for an online startup

We are a web startup building a SaaS application for the freight industry. The project is mainly dedicated to the paint the main form that our customer are using along the search results that the they get. All details are in the attached documents.
Updates
The application serves the Freight Forwarders community so please think towards this industry when using background images, banners, colors, icons, etc. Computer and technology images are irrelevant.
Customer fields at the top of the page is actually part of the form.
Target Market(s)
Usually business users (Sales people, procurement, shippers, freight forwarders). Some are less tech savvy and some appreciate the new trendy web apps.
Industry/Entity Type
Building
Colors
Designer to choose colors to be used in the design.
Look and feel
Each slider illustrates characteristics of the customer's brand and the style your logo design should communicate.

```html
<!DOCTYPE html>
<html lang="en">
<head>
<meta charset="utf-8">
<title>Cargoform – Quote Search</title>
<link href="https://fonts.googleapis.com/css2?family=Ubuntu:wght@400;500;700&display=swap" rel="stylesheet">
<style>
:root{
  --red:#c40000;
  --dark:#1c0a06;
  --black:#111;
  --band:#e6e6e6;
  --line:#d4d4d4;
  --text:#333;
  --blue:#2a5aa8;
  --yellow:#f7b500;
  --white:#fff;
}
*{box-sizing:border-box;margin:0;padding:0}
html,body{width:1099px;height:1200px;overflow:hidden;background:var(--white);font-family:'Ubuntu',sans-serif;color:var(--text)}
.page{position:relative;width:1099px;height:1200px}
.abs{position:absolute}
.topbar{left:0;top:0;width:1099px;height:39px;background:var(--white)}
.topbar .item{font-size:12px;color:#333}
.caret{display:inline-block;width:0;height:0;border-left:4px solid transparent;border-right:4px solid transparent;border-top:4px solid #333;margin-left:4px;vertical-align:middle}
.avatar{left:963px;top:1px;width:36px;height:36px;border-radius:50%;background:linear-gradient(#b9b9b9,#6a6a6a)}
.online{left:991px;top:27px;width:8px;height:8px;border-radius:50%;background:#3ac13a;border:1px solid #fff}
.hero{left:0;top:39px;width:1099px;height:517px;background:radial-gradient(ellipse at 78% 45%,#9a98a6 0%,#55505a 22%,#2c2428 48%,#161012 100%)}
.brand{left:112px;top:74px;font-size:29px;color:var(--white);font-weight:400}
.nav-home{left:510px;top:86px;width:41px;font-size:13px;font-weight:700;color:#fff;text-align:center;border-bottom:2px solid var(--red);padding-bottom:3px}
.nav-home svg{position:absolute;left:14px;top:-17px}
.nav-item{top:79px;height:29px;background:#fff;border-radius:2px;font-size:13px;color:#222;display:flex;align-items:center;justify-content:center}
.search-title{left:109px;top:272px;font-size:20px;color:#fff}
.search-input{left:109px;top:300px;width:343px;height:40px;background:#fff;border-radius:2px;font-size:12px;color:#888;padding:13px 8px}
.rate{left:110px;top:350px;font-size:12px;color:#fff;display:flex;align-items:center;gap:4px}
.cb{width:11px;height:11px;border:1px solid #999;background:#fff;display:inline-block}
.cb.on{background:#fff;border-color:#3a78b8;position:relative}
.tab{top:500px;height:56px;background:#f2f2f2;display:flex;align-items:center;gap:10px;padding-left:8px;font-size:13px;color:#222}
.tab .pic{width:44px;height:40px;border-radius:3px}
.more{left:822px;top:528px;width:59px;height:28px;background:var(--red);color:#fff;font-size:13px;display:flex;align-items:center;justify-content:center}
.thin{left:0;width:1099px;height:1px;background:var(--red)}
.colhead{left:0;top:595px;width:1099px;height:35px;background:var(--red)}
.colhead span{position:absolute;top:11px;font-size:13px;font-weight:700;color:#fff}
.qty{left:109px;top:666px;width:36px;height:22px;background:var(--black);color:#fff;font-size:13px;font-weight:500;text-align:center;line-height:22px}
.field{height:26px;background:#fff;border:1px solid #ccc;font-size:12px;color:#333;text-align:center;line-height:24px}
.select{left:320px;top:664px;width:193px;height:26px;background:#f0f0f0;border:1px solid #ddd;font-size:12px;line-height:24px;padding-left:9px}
.seg{height:26px;display:flex;align-items:center;justify-content:center;color:#fff;font-size:14px}
.seg.red{background:var(--red)}
.seg.blk{background:var(--black)}
.hr{left:0;width:1099px;height:1px;background:var(--line)}
.band{left:0;width:1099px;background:var(--band)}
.add-sq{left:108px;top:725px;width:32px;height:24px;background:var(--red);color:#fff;font-size:18px;text-align:center;line-height:24px}
.add-txt{left:140px;top:725px;width:146px;height:24px;background:#e4e4e4;font-size:13px;color:#222;line-height:24px;padding-left:18px}
.lbl{font-size:13px;color:#222}
.addr{height:37px;background:#fff;border:1px solid #ddd;font-size:13px;color:#333;padding:10px 10px}
.options{left:108px;top:972px;width:93px;height:32px;background:var(--dark);color:#fff;font-size:14px;line-height:32px;text-align:center}
.small{font-size:12px;color:#222;display:flex;align-items:center;gap:3px}
.radio{width:9px;height:9px;border:1px solid #888;border-radius:50%;display:inline-block}
.price{left:825px;top:988px;width:157px;height:24px;background:#fff;border:1px solid #ccc;font-size:12px;color:#555;line-height:22px;padding-left:6px}
.price i{position:absolute;right:3px;top:3px;width:16px;height:16px;border:1px solid #999;background:#eee}
.btn{top:1083px;height:39px;color:#fff;font-size:14px;font-weight:500;display:flex;align-items:center;justify-content:center}
.footer{left:0;top:1156px;width:1099px;height:44px;background:var(--dark)}
.footer span{position:absolute;top:15px;font-size:12px;color:#fff}
</style>
</head>
<body>
<div class="page">

  <div class="abs topbar">
    <svg class="abs" style="left:738px;top:10px" width="18" height="18" viewBox="0 0 18 18"><circle cx="8" cy="8" r="7" fill="none" stroke="#444" stroke-width="1.5"/><text x="8" y="12" font-size="10" text-anchor="middle" fill="#444" font-family="Ubuntu,sans-serif">$</text></svg>
    <span class="abs caret" style="left:754px;top:16px;margin:0"></span>
    <span class="abs item" style="left:795px;top:3px">English<span class="caret"></span></span>
    <span class="abs item" style="left:878px;top:12px;color:#2c4f7a">Alex.Rowan<span class="caret"></span></span>
    <div class="abs avatar" role="img" aria-label="User profile photo"></div>
    <div class="abs online"></div>
  </div>

  <div class="abs hero" role="img" aria-label="Photo of a white freight truck driving on a country road at dusk"></div>
  <div class="abs brand">Cargoform</div>
  <div class="abs nav-home"><svg width="12" height="11" viewBox="0 0 12 11"><path d="M6 0 12 5.5H10V11H7.5V7.5h-3V11H2V5.5H0Z" fill="#c40000"/></svg>HOME</div>
  <div class="abs nav-item" style="left:563px;width:85px">Menu Item1</div>
  <div class="abs nav-item" style="left:651px;width:84px">Menu Item2</div>
  <div class="abs nav-item" style="left:739px;width:84px">Menu Item3</div>
  <div class="abs nav-item" style="left:827px;width:84px">Menu Item4</div>
  <div class="abs nav-item" style="left:915px;width:83px">Menu Item5</div>

  <div class="abs search-title">Search for Quotes</div>
  <div class="abs search-input">Custome Name</div>
  <div class="abs rate"><span class="cb on"><svg class="abs" style="left:0;top:0" width="9" height="9" viewBox="0 0 9 9"><path d="M1 4.5 3.5 7 8 1.5" fill="none" stroke="#2a5aa8" stroke-width="1.6"/></svg></span>Rate quote?</div>

  <div class="abs tab" style="left:258px;width:150px"><div class="pic" role="img" aria-label="Wooden crate illustration" style="background:#c9a878"></div>Box or Pallet</div>
  <div class="abs tab" style="left:414px;width:191px"><div class="pic" role="img" aria-label="Boxes on a pallet illustration" style="background:#c8603a"></div>Shipping Container</div>
  <div class="abs tab" style="left:609px;width:205px"><div class="pic" role="img" aria-label="Gift parcel illustration" style="background:#9fd0e6;width:34px"></div>Envelop or small Parcel</div>
  <div class="abs more">MORE</div>

  <div class="abs thin" style="top:592px"></div>
  <div class="abs colhead">
    <span style="left:113px">QTY</span>
    <span style="left:191px">STACKABEL</span>
    <span style="left:320px">LOAD</span>
    <span style="left:554px">LENGHT</span>
    <span style="left:653px">WIDTH</span>
    <span style="left:740px">HEIGHT</span>
    <span style="left:873px">WEIGHT</span>
  </div>
  <div class="abs thin" style="top:632px"></div>

  <div class="abs qty">05</div>
  <span class="abs cb" style="left:219px;top:671px"></span>
  <div class="abs select">Box/Pallet</div>
  <div class="abs seg red" style="left:481px;top:664px;width:32px">
    <svg width="10" height="10" viewBox="0 0 10 10"><path d="M2 1 5 4 8 1M2 5 5 8 8 5" fill="none" stroke="#fff" stroke-width="1.6"/></svg></div>
  <div class="abs field" style="left:556px;top:665px;width:54px">100</div>
  <div class="abs field" style="left:646px;top:665px;width:54px">100</div>
  <div class="abs field" style="left:729px;top:665px;width:54px">100</div>
  <div class="abs seg red" style="left:786px;top:664px;width:43px">cm</div>
  <div class="abs seg blk" style="left:829px;top:664px;width:30px"><svg width="10" height="10" viewBox="0 0 10 10"><path d="M2 1 5 4 8 1M2 5 5 8 8 5" fill="none" stroke="#fff" stroke-width="1.6"/></svg></div>
  <div class="abs field" style="left:871px;top:665px;width:54px">100</div>
  <div class="abs seg red" style="left:928px;top:664px;width:41px">kg</div>
  <div class="abs seg blk" style="left:969px;top:664px;width:29px"><svg width="10" height="10" viewBox="0 0 10 10"><path d="M2 1 5 4 8 1M2 5 5 8 8 5" fill="none" stroke="#fff" stroke-width="1.6"/></svg></div>

  <div class="abs hr" style="top:710px"></div>
  <div class="abs add-sq">+</div>
  <div class="abs add-txt">ADD MORE UNITS</div>

  <div class="abs hr" style="top:764px"></div>
  <div class="abs band" style="top:767px;height:42px"></div>
  <div class="abs lbl" style="left:654px;top:782px">Total</div>
  <div class="abs field" style="left:696px;top:778px;width:54px;height:23px;line-height:21px">05</div>
  <div class="abs field" style="left:756px;top:778px;width:45px;height:23px;line-height:21px">01</div>
  <div class="abs seg blk" style="left:801px;top:778px;width:42px;height:23px">cm</div>
  <div class="abs seg red" style="left:843px;top:778px;width:29px;height:23px"><svg width="10" height="10" viewBox="0 0 10 10"><path d="M2 1 5 4 8 1M2 5 5 8 8 5" fill="none" stroke="#fff" stroke-width="1.6"/></svg></div>
  <div class="abs field" style="left:888px;top:778px;width:45px;height:23px;line-height:21px">100</div>
  <div class="abs seg blk" style="left:933px;top:778px;width:35px;height:23px">kg</div>
  <div class="abs seg red" style="left:968px;top:778px;width:30px;height:23px"><svg width="10" height="10" viewBox="0 0 10 10"><path d="M2 1 5 4 8 1M2 5 5 8 8 5" fill="none" stroke="#fff" stroke-width="1.6"/></svg></div>
  <div class="abs hr" style="top:812px"></div>

  <div class="abs hr" style="top:838px"></div>
  <div class="abs band" style="top:841px;height:80px"></div>
  <div class="abs lbl" style="left:109px;top:876px">From:</div>
  <div class="abs addr" style="left:147px;top:865px;width:316px">Shipping address or port</div>
  <svg class="abs" style="left:545px;top:862px" width="32" height="38" viewBox="0 0 32 38"><path d="M2 2 14 19 2 36H8L20 19 8 2Z" fill="#aaa"/><path d="M12 2 24 19 12 36H18L30 19 18 2Z" fill="#aaa"/></svg>
  <div class="abs lbl" style="left:651px;top:877px">To:</div>
  <div class="abs addr" style="left:673px;top:864px;width:316px">Shipping address or port</div>
  <div class="abs hr" style="top:923px"></div>

  <div class="abs hr" style="top:961px"></div>
  <div class="abs band" style="top:963px;height:81px"></div>
  <div class="abs options">OPTIONS</div>
  <div class="abs small" style="left:111px;top:1014px"><span class="radio"></span>Import</div>
  <div class="abs small" style="left:199px;top:1014px"><span class="radio"></span>Export</div>
  <div class="abs small" style="left:290px;top:1014px">Incoterm:&nbsp;<b style="color:var(--red)">FCA</b></div>
  <div class="abs small" style="left:441px;top:1012px"><span class="cb on" style="position:relative"><svg class="abs" style="left:0;top:0" width="9" height="9" viewBox="0 0 9 9"><path d="M1 4.5 3.5 7 8 1.5" fill="none" stroke="#2a8a3a" stroke-width="1.6"/></svg></span><svg width="16" height="16" viewBox="0 0 16 16"><circle cx="8" cy="8" r="7" fill="none" stroke="#222" stroke-width="1.5"/><path d="M3 3 13 13" stroke="#222" stroke-width="1.5"/></svg></div>
  <div class="abs small" style="left:494px;top:1012px"><span class="cb"></span><svg width="16" height="16" viewBox="0 0 16 16"><circle cx="8" cy="8" r="7" fill="none" stroke="#222" stroke-width="1.5"/><path d="M3 3 13 13" stroke="#222" stroke-width="1.5"/></svg></div>
  <div class="abs small" style="left:546px;top:1012px"><span class="cb"></span><svg width="16" height="16" viewBox="0 0 16 16"><circle cx="8" cy="8" r="7" fill="none" stroke="#222" stroke-width="1.5"/><path d="M3 3 13 13M13 3 3 13" stroke="#222" stroke-width="1.5"/></svg></div>
  <div class="abs price">Price level<i></i></div>
  <div class="abs" style="left:882px;top:1017px;width:100px;text-align:right;font-size:12px;color:#444">More options</div>
  <div class="abs hr" style="top:1046px"></div>

  <div class="abs btn" style="left:378px;width:160px;background:var(--blue);border-bottom:3px solid #1a3c78">SEARCH QUOTES</div>
  <div class="abs" style="left:550px;top:1094px;font-size:15px;color:#222">OR</div>
  <div class="abs btn" style="left:586px;width:187px;background:var(--yellow);border-bottom:3px solid #c98e00">CREATIVITY MANUALLY</div>

  <div class="abs footer">
    <span style="left:111px">About us</span>
    <span style="left:167px">Privacy policy</span>
    <span style="left:251px">Terms of service</span>
    <span style="left:349px">News</span>
    <span style="left:734px">Blog</span>
    <span style="left:770px">Friendwall</span>
    <span style="left:837px">Chirpline</span>
    <span style="left:899px">Worknet</span>
    <span style="left:950px">Cliptube</span>
  </div>

</div>
</body>
</html>
```